Postcard to Market Greeting Cards

Need a Postcard to
* Promote a particular human being and his story.
* Market and raise awareness of his art
* Advertise his website where the art can be purchased.

Background:
Rafi Domenkar is a refugee and artist trapped in a refugee camp in Indonesia.
He has committed no crimes. He had to escape his country as a refugee.
He is currently held in detention. The only way out is to be privately sponsored.
This costs a huge amount of money. Rafi is working to raise the money needed.
He is young and has lost 5 years being imprisoned. We must work to save him.

He draws everyday and sends the drawings to me. I make them into beautiful hand drawn art cards which we sell at markets, on the internet or via contacts.
He is not allowed to work. Secret drawing is the only way he can make a living.

This postcard is to
* share some of Rafi's Story and to give a sense of who he is.
* display his beautiful art cards which are sold for income via his website.
* Prominently display his website address as well as images of the cards.

These postcards will be given out at markets, letterbox dropped, sent to new customers, left in cafes and libraries etc so people will discover Rafi's Cards....
By buying the cards...Rafi can earn the funds he needs to pay for sponsorship into a free country. Many countries will accept him if he pays for the process.

Therefore...the postcard needs to be filled front and back. No need to leave space for address and postage. This leaves more room for samples of the Greeting Cards.

There is text provided for the front and back of the POSTCARD.
This may be edited and added to as the design process continues.

Images of Rafi's Cards have been uploaded for you.
It would be great if these can be beautifully and artistically presented on the postcard. The aim is to attract people to Rafi's hand drawn cards motivate people to want to buy them. Not all of the card images need to be used.

There are * black line cards * colour cards. * framed colour art works
so some of each could be promoted on the postcard.

Rafi's story will be included on the back of the card labelled for the Back.
A few words will be clearly and displayed on the front. Labelled fo the front.

The front art can be a single drawing image from Rafi OR a collage of many OR
It can contain his image or a few small images. See what you feel works well as there is scope to create a BEAUTIFUL postcard that depicts beautiful CARDS.

There is a quote from Rafi to be included on the front.
Can it be written in a handwriting style font to make it look like Rafi has written the message himself ?

There are images of Rafi to be used on the front and back.
Rafi's images have ben taken on dodgy phones and may not be a good quality.
They don't need to be large images and they DON'T need to all be used. There is a selection to choose from.

Rafi is in a prison. Maybe there are design elements that might remind of this.
Barbed wire maybe. Fences. The over all feel though is FREEDOM and BEAUTY in the hand drawn art cards and the escape they will provide in the end.

Rafi's website to be displayed on the front and back
lumevrodraws.example

email address on the back
helprafi2031@quillpost.example

These postcards will encourage buyers to read Rafi's story and want to help.
They will display beautifully hand drawn art cards which people will want to buy.
They will display the website address prominently and in some clever. arty way.

Good luck with it all.
I plan to increase first prize money depending on the designs....
and to offer more than first place depending on the deigns.

Please feel free to ask me any questions at any time.

Good luck and thanks for considering this project.

Tom Vaskell

Target Market(s)

Broad human rights supporters who will enjoy seeing a human story and will want to. respond.

Industry/Entity Type

Human Rights

Colors

Designer to choose colors to be used in the design.

Requirements
Must have
• Colourful and imaginative way of displaying the Greeting Cards being marketed by the Postcard. It is a taster and a sampling. They do not need to be arranged in rows or order..better to be creative in displaying the samples of cards. The website has the organised online shop. The postcard is a sampler and should MAKE people want to go to the website to buy the cards. The postcard must share the story of the artist.
• Handwriting font for the quote from the artist to make it look like he has written a personal message.
• Postcard needs to be filled on front and back. No blank space for mailing and address.
Nice to have
• Free and easy arty design. Photograph of the artist placed in some creative way.
Should not have
• Conservative structure. Free and arty is better.
• The postcard needs to be filled on the front and back ! No need to leave the bank area for mailing as it will only be used for marketing and distribution. it won't actually be used for mailing.

```html
<!DOCTYPE html>
<html lang="en">
<head>
<meta charset="utf-8">
<title>Free Rafi – Postcard</title>
<link rel="stylesheet" href="https://fonts.googleapis.com/css2?family=Amatic+SC:wght@400;700&family=Nothing+You+Could+Do&display=swap">
<style>
  :root {
    --paper: #ffffff;
    --ink: #1a1a1a;
    --ink-soft: #2e2e2e;
    --photo-light: #dcdcdc;
    --photo-dark: #3b3b3b;
    --bloom-orange: #ee5f26;
    --bloom-deep: #d9441c;
    --bloom-gold: #f3a832;
    --bird-yellow: #f2b531;
    --bird-black: #1f1a17;
    --leaf-green: #2f5b4c;
    --leaf-light: #8db25a;
    --twig-brown: #9a6a46;
  }
  * { margin: 0; padding: 0; box-sizing: border-box; }
  html, body { width: 1200px; height: 930px; overflow: hidden; background: var(--paper); }
  .postcard {
    position: relative;
    width: 1200px;
    height: 930px;
    background: var(--paper);
    color: var(--ink);
    font-family: "Amatic SC", cursive;
  }
  .headline {
    position: absolute;
    left: 62px;
    top: 52px;
    font-size: 90px;
    font-weight: 400;
    letter-spacing: 5px;
    line-height: 1;
    white-space: nowrap;
  }
  .subhead {
    position: absolute;
    left: 66px;
    top: 160px;
    font-size: 35px;
    font-weight: 400;
    line-height: 42px;
    letter-spacing: 0.6px;
    white-space: nowrap;
  }
  .quote {
    position: absolute;
    left: 96px;
    top: 280px;
    font-family: "Nothing You Could Do", cursive;
    font-size: 19px;
    line-height: 36px;
    color: var(--ink-soft);
    white-space: nowrap;
  }
  .quote-author {
    position: absolute;
    left: 318px;
    top: 607px;
    font-size: 27px;
    letter-spacing: 0.5px;
    white-space: nowrap;
  }
  .call-to-action {
    position: absolute;
    left: 60px;
    top: 680px;
    width: 426px;
    text-align: center;
    font-size: 30px;
    font-weight: 700;
    line-height: 36px;
    white-space: nowrap;
  }
  .website {
    position: absolute;
    left: 92px;
    top: 822px;
    font-size: 32px;
    letter-spacing: 8px;
    white-space: nowrap;
  }
  .collage-piece { position: absolute; }
  .artist-photo {
    left: 644px; top: 80px; width: 246px; height: 430px;
    border-radius: 48% 48% 12% 18%;
    background: linear-gradient(180deg, var(--photo-light) 0%, #8a8a8a 22%, var(--photo-dark) 40%, #4a4a4a 80%, #bdbdbd 100%);
    opacity: 0.9;
  }
  .blossom-branch {
    left: 880px; top: 76px; width: 284px; height: 372px;
    border-radius: 40% 55% 45% 60% / 35% 45% 55% 60%;
    background: radial-gradient(ellipse at 55% 45%, var(--bloom-orange) 0%, var(--bloom-gold) 55%, rgba(61,107,78,0.55) 80%, rgba(255,255,255,0) 100%);
  }
  .lily-bloom {
    left: 656px; top: 384px; width: 400px; height: 424px;
    border-radius: 50% 45% 48% 52%;
    background: radial-gradient(circle at 52% 48%, #b9a3c4 0%, var(--bloom-deep) 22%, var(--bloom-orange) 55%, var(--bloom-gold) 88%, rgba(255,255,255,0) 100%);
  }
  .songbird-pair {
    left: 500px; top: 312px; width: 276px; height: 584px;
    border-radius: 45% 55% 40% 60% / 30% 40% 60% 70%;
    background: linear-gradient(165deg, var(--leaf-green) 0%, var(--leaf-light) 20%, var(--bird-yellow) 42%, var(--bird-black) 62%, var(--bird-yellow) 80%, var(--twig-brown) 100%);
  }
  .warbler {
    left: 722px; top: 704px; width: 126px; height: 144px;
    border-radius: 50% 50% 45% 55%;
    background: linear-gradient(150deg, var(--bloom-orange) 0%, var(--leaf-light) 100%);
  }
  .perched-bird {
    left: 1012px; top: 632px; width: 164px; height: 280px;
    border-radius: 50% 50% 40% 40% / 35% 35% 65% 65%;
    background: linear-gradient(180deg, var(--bird-yellow) 0%, var(--bloom-orange) 60%, var(--twig-brown) 100%);
  }
</style>
</head>
<body>
  <main class="postcard">
    <h1 class="headline">FREE RAFI</h1>
    <p class="subhead">BUY RAFI'S BEAUTIFUL ART CARDS SUPPORT HIM<br>HELP RAFI PAY FOR HIS SPONSORSHIP TO FREEDOM</p>

    <blockquote class="quote">“It's true that my body is<br>prisoner....<br>But my thoughts and my<br>heart are not prisoner..<br>No one can imprison my<br>thoughts and my heart.<br>Because my thoughts and<br>my heart are with those<br>who I love them”</blockquote>
    <p class="quote-author">RAFI DOMENKAR</p>

    <p class="call-to-action">READ RAFI'S STORY AND<br>BUY HIS BEAUTIFUL HAND DRAWN A CARDS.<br>HELP SAVE A LIFE</p>
    <p class="website">WWW.LUMEVRODRAWS.EXAMPLE</p>

    <div class="collage-piece artist-photo" role="img" aria-label="Faded photograph of the artist in sunglasses and a dark t-shirt"></div>
    <div class="collage-piece blossom-branch" role="img" aria-label="Hand drawn branch of orange blossoms with green leaves"></div>
    <div class="collage-piece lily-bloom" role="img" aria-label="Hand drawn large orange lily with small lilac flowers"></div>
    <div class="collage-piece songbird-pair" role="img" aria-label="Hand drawn yellow and black songbirds on a branch among dark leaves"></div>
    <div class="collage-piece warbler" role="img" aria-label="Hand drawn small green and orange bird"></div>
    <div class="collage-piece perched-bird" role="img" aria-label="Hand drawn golden bird perched on a wooden post"></div>
  </main>
</body>
</html>
```